Brindle painting & waterproofing business card.

Business cards updated to reflect photos attached. we have given the photos of the old business cards and some of our updated designs for other items we have here in the office. Please see attached. if anyone needs to contact us directly for clarification you can email us at brindlerestoration@mailcove.example

Industry/Entity Type

Construction

Contact Information for Business Card

See attached photos

Font styles to use
Other font styles liked:
• Same as photos

Colors
ec1f27

Requirements
Must have
• Employee Names,
• Dennis Marlow II, Supervisor/Owner
• Dee Marlow, President/Owner
• Gus Tremby, Sales Representative
• Lyle Varsen, Supervisor
• Change 20 years to 25
Nice to have
• ideas reflecting the attached photos
Should not have
• should not be exactly like attached photos as those are old business card but reflect to match new logo listed as korvel van and cup photo.

```html
<!DOCTYPE html>
<html lang="en">
<head>
<meta charset="utf-8">
<title>Brindle's Painting &amp; Waterproofing – Business Card</title>
<link href="https://fonts.googleapis.com/css2?family=Roboto+Condensed:wght@400;700;900&family=Tinos&display=swap" rel="stylesheet">
<style>
  :root {
    --brand-red: #ec1f27;
    --deep-red: #a3141b;
    --ink: #1d1d1d;
    --card-white: #f7f7f7;
    --stage: #e6e2dc;
    --shadow: rgba(0,0,0,0.28);
  }
  html, body {
    margin: 0;
    width: 1200px;
    height: 780px;
    overflow: hidden;
    background: var(--stage);
    font-family: "Roboto Condensed", Arial, sans-serif;
  }
  .canvas { position: relative; width: 1200px; height: 780px; }
  .card {
    position: absolute;
    width: 540px;
    height: 310px;
    border-radius: 18px;
    overflow: hidden;
    background: var(--card-white);
    box-shadow: 0 10px 24px var(--shadow);
  }
  .card-front { left: 50px; top: 70px; }
  .card-back { left: 610px; top: 400px; }
  .card-art { position: absolute; inset: 0; }

  /* front */
  .brand-block { position: absolute; left: 0; top: 18px; width: 540px; text-align: center; }
  .brand-name {
    margin: 0;
    font-weight: 900;
    font-size: 62px;
    line-height: 1;
    letter-spacing: 1px;
    color: var(--brand-red);
  }
  .brand-service {
    margin: 4px 0 0;
    font-family: "Tinos", "Times New Roman", serif;
    font-size: 13px;
    letter-spacing: 1px;
    color: var(--ink);
  }
  .brand-tagline {
    margin: 1px 0 0;
    font-family: "Tinos", "Times New Roman", serif;
    font-size: 16px;
    letter-spacing: 0.8px;
    color: var(--ink);
  }
  .contact-block {
    position: absolute;
    left: 0; top: 150px; width: 540px;
    text-align: center;
    color: #fff;
  }
  .person-name { margin: 0; font-weight: 700; font-size: 22px; letter-spacing: 0.5px; }
  .person-role { margin: 0; font-size: 13px; letter-spacing: 0.5px; }
  .credential { margin: 2px 0 0; font-weight: 700; font-size: 13px; }
  .credential .license { font-weight: 400; }
  .contact-line { margin: 4px 0 0; font-size: 12px; font-weight: 700; }
  .address {
    position: absolute; left: 0; top: 272px; width: 540px;
    margin: 0; text-align: center;
    font-size: 13px; font-weight: 700; letter-spacing: 0.4px;
    color: var(--ink);
  }

  /* back */
  .logo-lockup {
    position: absolute; left: 0; top: 50px; width: 540px;
    text-align: center;
    color: var(--brand-red);
    font-weight: 900;
    text-transform: uppercase;
    line-height: 0.95;
  }
  .logo-lockup .logo-name { display: block; font-size: 70px; }
  .logo-lockup .logo-sub { display: block; font-size: 34px; letter-spacing: 2px; }
  .website {
    position: absolute; left: 40px; bottom: 18px;
    margin: 0;
    font-size: 14px; font-weight: 700; letter-spacing: 3px;
    color: #fff;
  }
  .website .tld { font-weight: 400; font-size: 12px; letter-spacing: 2px; }
</style>
</head>
<body>
<main class="canvas">

  <section class="card card-front" aria-label="Business card front">
    <svg class="card-art" viewBox="0 0 540 310" aria-hidden="true">
      <defs>
        <linearGradient id="frontBand" x1="0" y1="0" x2="1" y2="1">
          <stop offset="0" stop-color="#b5151c"/>
          <stop offset="0.5" stop-color="#ec1f27"/>
          <stop offset="1" stop-color="#9e1219"/>
        </linearGradient>
        <linearGradient id="frontPaper" x1="0" y1="0" x2="0" y2="1">
          <stop offset="0" stop-color="#ffffff"/>
          <stop offset="1" stop-color="#ececec"/>
        </linearGradient>
      </defs>
      <rect width="540" height="310" fill="url(#frontPaper)"/>
      <path d="M0,150 Q270,118 540,140 L540,252 Q270,282 0,262 Z" fill="url(#frontBand)"/>
      <path d="M0,150 Q270,118 540,140" fill="none" stroke="#111" stroke-width="2"/>
      <path d="M0,262 Q270,282 540,252" fill="none" stroke="#111" stroke-width="2"/>
      <path d="M0,230 Q220,170 540,210 L540,252 Q270,282 0,262 Z" fill="#fff" opacity="0.06"/>
    </svg>
    <div class="brand-block">
      <p class="brand-name">BRINDLE'S</p>
      <p class="brand-service">PAINTING</p>
      <p class="brand-tagline">WATERPROOFING &amp; CONCRETE RESTORATION</p>
    </div>
    <div class="contact-block">
      <p class="person-name">DENNIS MARLOW II</p>
      <p class="person-role">SUPERVISOR/OWNER</p>
      <p class="credential">GENERAL CONTRACTOR <span class="license">CGC#7730418</span></p>
      <p class="credential">LICENSED &amp; INSURED</p>
      <p class="contact-line">O: 555.204.7135 | M: 555.318.0264 | E: brindlerestoration@mailcove.example</p>
    </div>
    <p class="address">418 GULLWING AVE, CORAL BEND, FL 39021</p>
  </section>

  <section class="card card-back" aria-label="Business card back">
    <svg class="card-art" viewBox="0 0 540 310" aria-hidden="true">
      <defs>
        <linearGradient id="backBand" x1="0" y1="0" x2="1" y2="0">
          <stop offset="0" stop-color="#ec1f27"/>
          <stop offset="1" stop-color="#a3141b"/>
        </linearGradient>
        <radialGradient id="backPaper" cx="0.6" cy="0.4" r="0.8">
          <stop offset="0" stop-color="#ffffff"/>
          <stop offset="1" stop-color="#e4e4e4"/>
        </radialGradient>
      </defs>
      <rect width="540" height="310" fill="url(#backPaper)"/>
      <path d="M0,226 Q260,300 540,292 L540,310 L0,310 Z" fill="#a3141b"/>
      <path d="M0,236 Q260,308 540,300 L540,310 L0,310 Z" fill="url(#backBand)"/>
      <path d="M0,222 Q260,296 540,288" fill="none" stroke="#111" stroke-width="2"/>
      <path d="M0,214 Q260,288 540,280" fill="none" stroke="#ec1f27" stroke-width="2"/>
    </svg>
    <h1 class="logo-lockup">
      <span class="logo-name">Brindle's</span>
      <span class="logo-sub">Painting &amp; Restoration</span>
    </h1>
    <p class="website">www.BRINDLERESTORATION<span class="tld">.example</span></p>
  </section>

</main>
</body>
</html>
```